Looking for an amazing business card for a thriving DJ business

We need a business card design for a DJ company based in South Florida. The DJ company specializes in weddings, parties, bar mitzvahs, corporate events, proms, and reunions. We are looking for a modern, simple business card design. The card should state DJ Marlow K.
Updates

The name on the card should be DJ Marlow K

Industry/Entity Type

Entertainment Industry

Contact Information for Business Card

DJ Marlow K
512.447.2086
atxdjmarlowk@quellmail.com
https://www.facebook.com/DjMarlowK/
https://www.instagram.com/djmarlow.k/
www.djmarlowk.net

Font styles to use
Serif
Sans Serif

Requirements
Must have
• My business card has to be awesome.
Should not have
• The card has to have personality.

```html
<!DOCTYPE html>
<html lang="en">
<head>
<meta charset="utf-8">
<title>DJ Marlow K – Business Card</title>
<link href="https://fonts.googleapis.com/css2?family=Poppins:wght@400;500&display=swap" rel="stylesheet">
<style>
  :root {
    --backdrop: #1d1c21;
    --violet-deep: #2a1350;
    --violet: #4b2a8a;
    --violet-light: #6a45b0;
    --club-blue: #2b3fb8;
    --club-pink: #b04fc4;
    --club-ice: #a9c4ff;
    --gold: #d9a441;
    --white: #ffffff;
    --ink: #2a2a2a;
  }
  * { box-sizing: border-box; margin: 0; padding: 0; }
  html, body {
    width: 1200px; height: 800px; overflow: hidden;
    background: var(--backdrop);
    font-family: "Poppins", sans-serif;
  }
  .canvas {
    width: 1200px; height: 800px;
    display: flex; align-items: center; justify-content: center; gap: 40px;
  }
  .card {
    position: relative;
    width: 540px; height: 310px;
    border-radius: 22px;
    overflow: hidden;
    box-shadow: 0 18px 40px rgba(0,0,0,.55);
  }
  .club-photo {
    position: absolute; inset: 0;
    background:
      radial-gradient(circle at 28% 30%, var(--club-ice) 0%, rgba(169,196,255,0) 30%),
      radial-gradient(circle at 20% 75%, var(--club-pink) 0%, rgba(176,79,196,0) 35%),
      radial-gradient(circle at 80% 25%, var(--club-pink) 0%, rgba(176,79,196,0) 30%),
      linear-gradient(135deg, var(--club-blue) 0%, #1b2a8c 55%, #121a5e 100%);
  }
  .brand-seal {
    position: absolute;
    width: 150px; height: 150px; border-radius: 50%;
    background: var(--white);
    display: flex; align-items: center; justify-content: center;
    text-align: center;
  }
  .brand-seal .brand-name {
    font-weight: 500; font-size: 18px; line-height: 1.2;
    color: var(--ink);
  }
  .card-front .brand-seal { left: 195px; top: 80px; }

  .card-back {
    background: linear-gradient(140deg, var(--violet-light) 0%, var(--violet) 45%, var(--violet-deep) 100%);
  }
  .card-back .brand-seal { left: 50px; top: 95px; width: 140px; height: 140px; }
  .divider {
    position: absolute; left: 232px; top: 60px;
    width: 1px; height: 190px; background: rgba(255,255,255,.7);
  }
  .contact-block {
    position: absolute; left: 255px; top: 52px;
    color: var(--white);
  }
  .holder-name {
    font-weight: 500; font-size: 26px; letter-spacing: .3px;
    margin-bottom: 14px; white-space: nowrap;
  }
  .contact-list { list-style: none; }
  .contact-list li {
    display: flex; align-items: center; gap: 12px;
    font-size: 12.5px; height: 27px; white-space: nowrap;
  }
  .contact-list svg { width: 15px; height: 15px; flex: none; }
</style>
</head>
<body>
<main class="canvas">
  <section class="card card-front">
    <div class="club-photo" role="img" aria-label="Nightclub scene with DJ decks, laser lights and a dancing crowd in blue and pink light"></div>
    <div class="brand-seal"><span class="brand-name">Spinwell<br>Events</span></div>
  </section>

  <section class="card card-back">
    <div class="brand-seal"><span class="brand-name">Spinwell<br>Events</span></div>
    <div class="divider"></div>
    <div class="contact-block">
      <h1 class="holder-name">DJ Marlow K</h1>
      <ul class="contact-list">
        <li>
          <svg viewBox="0 0 16 16" aria-hidden="true"><path d="M4 1.5l2.2 3-1.3 1.6a9 9 0 0 0 5 5l1.6-1.3 3 2.2-1.2 2.5C7.5 14.8 1.2 8.5 1.5 2.7z" fill="var(--gold)"/></svg>
          512.447.2086
        </li>
        <li>
          <svg viewBox="0 0 16 16" aria-hidden="true"><rect x="1" y="3" width="14" height="10" rx="1" fill="var(--gold)"/><path d="M1.5 3.5L8 9l6.5-5.5" fill="none" stroke="var(--violet-deep)" stroke-width="1.2"/></svg>
          atxdjmarlowk@quellmail.com
        </li>
        <li>
          <svg viewBox="0 0 16 16" aria-hidden="true"><g fill="none" stroke="var(--gold)" stroke-width="1.6" stroke-linecap="round"><path d="M6.8 9.2a2.6 2.6 0 0 0 3.7 0l2.6-2.6a2.6 2.6 0 0 0-3.7-3.7l-1 1"/><path d="M9.2 6.8a2.6 2.6 0 0 0-3.7 0L2.9 9.4a2.6 2.6 0 0 0 3.7 3.7l1-1"/></g></svg>
          DjMarlowK
        </li>
        <li>
          <svg viewBox="0 0 16 16" aria-hidden="true"><g fill="none" stroke="var(--gold)" stroke-width="1.6" stroke-linecap="round"><path d="M6.8 9.2a2.6 2.6 0 0 0 3.7 0l2.6-2.6a2.6 2.6 0 0 0-3.7-3.7l-1 1"/><path d="M9.2 6.8a2.6 2.6 0 0 0-3.7 0L2.9 9.4a2.6 2.6 0 0 0 3.7 3.7l1-1"/></g></svg>
          djmarlow.k
        </li>
        <li>
          <svg viewBox="0 0 16 16" aria-hidden="true"><g fill="none" stroke="var(--gold)" stroke-width="1.3"><circle cx="8" cy="8" r="6.3"/><ellipse cx="8" cy="8" rx="2.8" ry="6.3"/><path d="M1.7 8h12.6M2.8 4.8h10.4M2.8 11.2h10.4"/></g></svg>
          www.djmarlowk.net
        </li>
      </ul>
    </div>
  </section>
</main>
</body>
</html>
```